Modern & Innovative business card for new commercial construction company Valdorne - Inc.
Valdorne-Inc
Modern & Innovative business card for new commercial construction company Valdorne - Inc. - Construction
Creative Brief
Professional
Marcus T. Whitfield
President
P.O. Box 3097 Brenmoor, W.R. 27519-3097
MWhitfield@valdorne-inc.example
Either the logo over the entire back of the card with the contact information on the front.

```html
<!DOCTYPE html>
<html lang="en">
<head>
<meta charset="utf-8">
<title>Valdorne Inc. Business Card</title>
<link rel="stylesheet" href="https://fonts.googleapis.com/css2?family=Michroma&display=swap">
<style>
  :root {
    --page-bg: #e9e9e9;
    --card-bg: #ffffff;
    --brand-red: #d3262f;
    --brand-red-dark: #a81c23;
    --steel: #9a9a9a;
    --steel-light: #cfcfcf;
    --ink: #555555;
    --ink-soft: #777777;
  }
  * { box-sizing: border-box; margin: 0; padding: 0; }
  html, body {
    width: 1200px; height: 914px; overflow: hidden;
    background: var(--page-bg);
    font-family: "Michroma", sans-serif;
  }
  .card {
    position: absolute;
    left: 100px; top: 171px;
    width: 1000px; height: 572px;
    background: var(--card-bg);
    box-shadow: 0 6px 24px rgba(0,0,0,0.18);
    overflow: hidden;
  }
  .brand {
    position: absolute;
    left: 80px; top: 190px;
    display: flex; align-items: center; gap: 18px;
  }
  .brand-dot {
    width: 64px; height: 64px; border-radius: 50%;
    border: 8px solid var(--brand-red);
    flex: none;
  }
  .brand-name {
    font-size: 22px; color: var(--ink);
    letter-spacing: 1px; line-height: 1.3;
    text-transform: uppercase;
  }
  .divider {
    position: absolute;
    left: 425px; top: 160px;
    width: 2px; height: 215px;
    background: linear-gradient(var(--steel-light), var(--steel), var(--steel-light));
  }
  .contact-block {
    position: absolute;
    left: 450px; top: 165px;
    width: 520px;
  }
  .person-name {
    font-size: 17px; color: var(--brand-red);
    letter-spacing: 2px; text-transform: uppercase;
    white-space: nowrap;
  }
  .person-title {
    font-size: 12px; color: var(--ink-soft);
    margin-top: 6px; text-transform: uppercase; letter-spacing: 1px;
  }
  .contact-list {
    list-style: none; margin-top: 28px;
  }
  .contact-item {
    display: flex; align-items: flex-start; gap: 10px;
    font-size: 12px; color: var(--ink);
    line-height: 22px; text-transform: uppercase; letter-spacing: 0.5px;
    white-space: nowrap;
  }
  .contact-icon { flex: none; margin-top: 3px; }
  .indent { padding-left: 26px; }
  .card-bands {
    position: absolute; left: 0; bottom: 0;
  }
</style>
</head>
<body>
  <div class="card">
    <div class="brand">
      <span class="brand-dot"></span>
      <span class="brand-name">Valdorne<br>Inc.</span>
    </div>

    <div class="divider"></div>

    <div class="contact-block">
      <div class="person-name">Marcus T. Whitfield</div>
      <div class="person-title">President</div>
      <ul class="contact-list">
        <li class="contact-item">
          <svg class="contact-icon" width="16" height="16" viewBox="0 0 16 16"><circle cx="8" cy="8" r="8" fill="var(--brand-red)"/><path d="M8 3.5a3 3 0 0 0-3 3c0 2.2 3 5.5 3 5.5s3-3.3 3-5.5a3 3 0 0 0-3-3z" fill="#fff"/><circle cx="8" cy="6.5" r="1.1" fill="var(--brand-red)"/></svg>
          <span>P.O. Box 3097</span>
        </li>
        <li class="contact-item indent">Brenmoor, W.R. 27519-3097</li>
        <li class="contact-item">
          <svg class="contact-icon" width="16" height="16" viewBox="0 0 16 16"><circle cx="8" cy="8" r="8" fill="var(--brand-red)"/><path d="M5.3 4.2l1.4-.3.9 2-1 .8a5 5 0 0 0 2.5 2.5l.8-1 2 .9-.3 1.4c-3.3.4-6.7-3-6.3-6.3z" fill="#fff"/></svg>
          <span>555.555.0142</span>
        </li>
        <li class="contact-item">
          <svg class="contact-icon" width="16" height="16" viewBox="0 0 16 16"><circle cx="8" cy="8" r="8" fill="var(--brand-red)"/><rect x="4" y="5" width="8" height="6" fill="#fff"/><path d="M4 5l4 3.2L12 5" fill="none" stroke="var(--brand-red)" stroke-width="1"/></svg>
          <span>MWhitfield@valdorne-inc.example</span>
        </li>
        <li class="contact-item">
          <svg class="contact-icon" width="16" height="16" viewBox="0 0 16 16"><circle cx="8" cy="8" r="8" fill="var(--brand-red)"/><circle cx="8" cy="8" r="4" fill="none" stroke="#fff" stroke-width="1.2"/><path d="M4 8h8M8 4c-1.6 2.4-1.6 5.6 0 8M8 4c1.6 2.4 1.6 5.6 0 8" fill="none" stroke="#fff" stroke-width="0.9"/></svg>
          <span>www.valdorne-inc.example</span>
        </li>
      </ul>
    </div>

    <svg class="card-bands" width="1000" height="180" viewBox="0 0 1000 180">
      <defs>
        <linearGradient id="steelBand" x1="0" y1="0" x2="0" y2="1">
          <stop offset="0" stop-color="#d9d9d9"/>
          <stop offset="0.5" stop-color="#a6a6a6"/>
          <stop offset="1" stop-color="#7d7d7d"/>
        </linearGradient>
        <linearGradient id="redBand" x1="0" y1="0" x2="0" y2="1">
          <stop offset="0" stop-color="var(--brand-red)"/>
          <stop offset="1" stop-color="var(--brand-red-dark)"/>
        </linearGradient>
      </defs>
      <rect x="0" y="30" width="1000" height="6" fill="var(--brand-red)"/>
      <polygon points="0,70 600,70 640,110 1000,110 1000,180 0,180" fill="url(#steelBand)"/>
      <polygon points="0,70 600,70 640,110 640,180 0,180" fill="url(#redBand)"/>
    </svg>
  </div>
</body>
</html>
```